Business card and stationery design

Harbour & Summit Planners is a leading event and conference design and management company.
Please view harbourandsummit.com.au

The business cards needs to convey:
- professionalism and competency
- exclusivity
- memorable experiences and quality

The business card needs to have the following aspects:
- double sided
- Full colour CMYK
- Printed on either high gloss matt card (designer to recommend)

For the business stationery we require:
- Letterhead with top banner and bottom footer
- A thank you card design
- a with compliments slip design
- a MS powerpoint and MS publisher client presentation slide design which includes cover page and then a standard presentation page
(Note- we do NOT require an envelope design- who sends letters these days!)

The company image is using the key colours of gold, silver and black.
A black background to the business card has been used before and is preferred although we are open to options.

Target Market(s)

High end corporations and businesses that require their events and conferences to be exceptionally well designed and managed

Industry/Entity Type

Business

Contact Information for Business Card

FRONT:

Darcy Whitlam
- Event and Conference Specialist

Mobile- +61 (0) 491 362 047
Office- 1300 586 917
darcyw@harbourandsummit.com.au

Web- harbourandsummit.com.au

BACK:

- Event and

Font styles to use
Other font styles liked:
• The logo designer used Trajan Pro Bold 3 for the font text in the logo

Requirements
Must have
• Amazing design of the following:
• - business card (double sided)
• - letterhead
• - client thank you card
• - powerpoint and publisher client presentation design files

```html
<!DOCTYPE html>
<html lang="en">
<head>
<meta charset="utf-8">
<title>Harbour &amp; Summit Planners — Business Card</title>
<link rel="stylesheet" href="https://fonts.googleapis.com/css2?family=Cinzel:wght@700&family=Montserrat:wght@700&family=Questrial&display=swap">
<style>
  :root {
    --backdrop: #1a1a1a;
    --card: #0b0b0b;
    --card-sheen: #242424;
    --gold: #c9a43a;
    --silver: #d6d6d6;
    --white: #f2f2f2;
  }
  * { margin: 0; padding: 0; box-sizing: border-box; }
  html, body {
    width: 1200px; height: 969px; overflow: hidden;
    background: var(--backdrop);
  }
  .canvas { position: relative; width: 1200px; height: 969px; }

  .card {
    position: absolute;
    width: 640px; height: 366px;
    border-radius: 22px;
    background: linear-gradient(100deg, var(--card) 0%, var(--card) 35%, var(--card-sheen) 48%, var(--card) 62%, var(--card) 100%);
    box-shadow: 0 18px 40px rgba(0,0,0,.55);
    overflow: hidden;
  }
  .card-back  { left: 440px; top: 70px; }
  .card-front { left: 120px; top: 520px; }

  .brand {
    display: flex; align-items: center; gap: 14px;
    font-family: "Cinzel", serif; font-weight: 700;
    color: var(--silver);
    letter-spacing: 1px;
  }
  .brand-dot { flex: none; border-radius: 50%; background: var(--gold); }

  .card-back .brand {
    position: absolute; left: 0; right: 0; top: 130px;
    justify-content: center; font-size: 30px;
  }
  .card-back .brand-dot { width: 26px; height: 26px; }
  .card-back .web {
    position: absolute; left: 0; right: 0; top: 212px;
    text-align: center;
    font-family: "Questrial", sans-serif; font-size: 19px; color: var(--white);
  }
  .web .domain { color: var(--gold); }

  .card-front .brand {
    position: absolute; left: 34px; top: 132px; width: 240px;
    font-size: 22px; line-height: 1.25; flex-wrap: nowrap;
  }
  .card-front .brand-dot { width: 20px; height: 20px; }
  .divider {
    position: absolute; left: 300px; top: 50px;
    width: 1.5px; height: 250px;
    background: linear-gradient(to bottom, transparent, var(--gold) 25%, var(--gold) 75%, transparent);
  }
  .contact {
    position: absolute; left: 326px; top: 78px;
    font-family: "Questrial", sans-serif; color: var(--white);
  }
  .contact .name {
    font-family: "Montserrat", sans-serif; font-weight: 700;
    font-size: 20px; color: var(--gold); text-transform: uppercase; letter-spacing: .5px;
  }
  .contact .role { font-size: 17px; margin-bottom: 22px; }
  .contact ul { list-style: none; }
  .contact li {
    display: flex; align-items: center; gap: 10px;
    font-size: 16px; line-height: 28px;
  }
  .contact svg { width: 16px; height: 16px; flex: none; }
</style>
</head>
<body>
<main class="canvas">

  <section class="card card-back" aria-label="Card back">
    <div class="brand"><span class="brand-dot"></span>Harbour &amp; Summit Planners</div>
    <p class="web">www.<span class="domain">harbourandsummit</span>.com.au</p>
  </section>

  <section class="card card-front" aria-label="Card front">
    <div class="brand"><span class="brand-dot"></span><span>Harbour &amp; Summit Planners</span></div>
    <div class="divider"></div>
    <div class="contact">
      <p class="name">Darcy Whitlam</p>
      <p class="role">Event and Conference Specialist</p>
      <ul>
        <li>
          <svg viewBox="0 0 16 16" aria-hidden="true"><rect x="4" y="1" width="8" height="14" rx="1.5" fill="none" stroke="var(--gold)" stroke-width="1.5"/><circle cx="8" cy="12.5" r="0.9" fill="var(--gold)"/></svg>
          +61 (0) 491 362 047
        </li>
        <li>
          <svg viewBox="0 0 16 16" aria-hidden="true"><path d="M2 6c0-2 3-3 6-3s6 1 6 3l-2 1-1.5-2h-5L4 7z" fill="var(--gold)"/><rect x="3.5" y="8" width="9" height="6" rx="1" fill="var(--gold)"/></svg>
          1300 586 917
        </li>
        <li>
          <svg viewBox="0 0 16 16" aria-hidden="true"><rect x="1" y="3" width="14" height="10" rx="1" fill="var(--gold)"/><path d="M1.5 3.5 8 9l6.5-5.5" fill="none" stroke="var(--card)" stroke-width="1.2"/></svg>
          darcyw@harbourandsummit.com.au
        </li>
        <li>
          <svg viewBox="0 0 16 16" aria-hidden="true"><circle cx="8" cy="8" r="6.5" fill="none" stroke="var(--gold)" stroke-width="1.3"/><ellipse cx="8" cy="8" rx="3" ry="6.5" fill="none" stroke="var(--gold)" stroke-width="1"/><path d="M1.5 8h13" stroke="var(--gold)" stroke-width="1"/></svg>
          <span class="web">www.<span class="domain">harbourandsummit</span>.com.au</span>
        </li>
      </ul>
    </div>
  </section>

</main>
</body>
</html>
```